Classic and neutral book cover design

We are looking for a classic and neutral book cover design to be used as the template for a series of books to be published. We are hence looking for a template that will allow us to easily change the title name for all books in this series.
The use of very few colours (black and white is welcome) and few design elements is a big bonus. As a source of inspiration we would like to ask you to view the very simple and
If you think you have a cool idea that can add a twist to the formal classic look don't hesitate. Go for it !
Work will be done for a 30 year old Sweden based cultural non-profit called VĂ©ru (www.veruhaus-example.org). We work with the publishing and supporting of post-modern art and literature addressing contemporary topics but are also involved in assisting projects of cultural preservation.
Target Market(s)
The audience is expected to have some form of interest in culture but could range from hobbyist readers to tenure track scholars
Industry/Entity Type
Non-Profit
Requirements
Must have
- General:
- Classic and neutral feel
- Preferably very simple and few shapes
- usage of few colours (black and white is welcome)
Information to be displayed on the cover is:
- Author
- Title
- type of work e.g. play/novel (optional)
- publishing house (in this case "Veru Publishing")
Nice to have
- ideas to prevent it from become boring are of course welcome
Should not have
- - too many colours

```html
<!DOCTYPE html>
<html lang="en">
<head>
<meta charset="utf-8">
<title>Book Cover Template</title>
<link href="https://fonts.googleapis.com/css2?family=Open+Sans:wght@600;700;800&display=swap" rel="stylesheet">
<style>
  :root {
    --ink: #111111;
    --paper: #e7e7e7;
    --paper-soft: #dcdcdc;
    --stage: #f2f2f2;
    --white: #ffffff;
  }
  html, body {
    margin: 0;
    width: 1200px;
    height: 800px;
    overflow: hidden;
    background: var(--stage);
    font-family: "Open Sans", Arial, sans-serif;
  }
  .cover-spread {
    position: absolute;
    left: 228px;
    top: 128px;
    display: flex;
    height: 544px;
    box-shadow: 0 6px 24px rgba(0,0,0,0.12);
  }
  /* Back cover */
  .back-cover {
    width: 340px;
    height: 544px;
    background: var(--paper);
    color: var(--ink);
    box-sizing: border-box;
    padding: 20px 14px 0;
    position: relative;
    text-align: center;
  }
  .back-author {
    font-weight: 700;
    font-size: 14px;
    line-height: 1;
    margin-left: 140px;
    text-align: left;
  }
  .back-title {
    font-weight: 800;
    font-size: 50px;
    line-height: 0.95;
    letter-spacing: 1px;
  }
  .back-type {
    font-weight: 700;
    font-size: 19px;
    line-height: 1.1;
    margin-bottom: 10px;
  }
  .back-blurb {
    font-weight: 700;
    font-size: 10.3px;
    line-height: 1.42;
    text-align: justify;
    text-align-last: center;
    margin: 0;
  }
  .back-boxes {
    position: absolute;
    left: 24px;
    right: 14px;
    bottom: 22px;
    display: flex;
    justify-content: space-between;
  }
  .back-box {
    width: 108px;
    height: 58px;
    background: var(--ink);
    color: var(--white);
    font-size: 11px;
    font-weight: 600;
    display: flex;
    align-items: center;
    justify-content: center;
    letter-spacing: 0.5px;
  }
  /* Spine */
  .spine {
    width: 44px;
    height: 544px;
    background: linear-gradient(90deg, var(--paper-soft), var(--paper));
    position: relative;
    border-left: 1px solid #cfcfcf;
    border-right: 1px solid #cfcfcf;
  }
  .spine-title, .spine-author {
    position: absolute;
    left: 50%;
    transform: translateX(-50%) rotate(90deg);
    transform-origin: center;
    white-space: nowrap;
    color: var(--ink);
    font-weight: 800;
  }
  .spine-title { top: 280px; top: 62px; font-size: 26px; letter-spacing: 3px; }
  .spine-author { top: 470px; font-size: 10px; letter-spacing: 1px; font-weight: 700; }
  /* Front cover */
  .front-cover { width: 340px; height: 544px; display: block; }
  .front-cover text { font-family: "Open Sans", Arial, sans-serif; }
</style>
</head>
<body>
  <main class="cover-spread">
    <section class="back-cover">
      <div class="back-author">AUTHOR</div>
      <div class="back-title">TITLE</div>
      <div class="back-type">TYPE OF WORK</div>
      <p class="back-blurb">Lorem ipsum dolor sit amet, consectetur adipisicing elit, sed do eiusmod tempor incididunt ut labore et dolore magna aliqua. Ut enim ad minim veniam, quis nostrud exercitation. Lorem ipsum dolor sit amet, consectetur adipisicing elit, sed do eiusmod tempor incididunt ut labore et dolore magna aliqua. Ut enim ad minim veniam, quis nostrud exercitation. Lorem ipsum dolor sit amet, consectetur adipisicing elit, sed do eiusmod tempor incididunt ut labore et dolore magna aliqua. Ut enim ad minim veniam, quis nostrud exercitation. Lorem ipsum dolor sit amet, consectetur adipisicing elit, sed do eiusmod tempor incididunt ut labore et dolore magna aliqua. Ut enim ad minim veniam, quis nostrud exercitation. Lorem ipsum dolor sit amet, consectetur adipisicing elit, sed do eiusmod tempor incididunt ut labore et dolore magna aliqua. Ut enim ad minim veniam, quis nostrud exercitation. Lorem ipsum dolor sit amet, consectetur adipisicing elit, sed do eiusmod tempor incididunt ut labore et dolore magna aliqua. Ut enim ad minim veniam, quis nostrud exercitation.</p>
      <div class="back-boxes">
        <div class="back-box">LOGO</div>
        <div class="back-box">ISBN</div>
      </div>
    </section>

    <section class="spine">
      <div class="spine-title">TITLE</div>
      <div class="spine-author">AUTHOR</div>
    </section>

    <svg class="front-cover" viewBox="0 0 400 640" xmlns="http://www.w3.org/2000/svg">
      <defs>
        <path id="type-arc" d="M 48 392 A 152 152 0 0 1 352 392"/>
      </defs>
      <rect class="front-ground" x="0" y="0" width="400" height="640" fill="var(--paper)"/>
      <rect class="front-top-band" x="0" y="0" width="400" height="36" fill="var(--ink)"/>
      <text class="front-publisher" x="390" y="24" text-anchor="end" font-size="12" font-weight="700" fill="var(--white)">Publishing House</text>
      <text class="front-title" x="200" y="168" text-anchor="middle" font-size="70" font-weight="800" letter-spacing="3" fill="var(--ink)">TITLE</text>
      <rect class="front-lower-band" x="0" y="373" width="400" height="267" fill="var(--ink)"/>
      <circle class="front-ring" cx="200" cy="392" r="142" fill="var(--ink)"/>
      <circle class="front-image-slot" cx="200" cy="392" r="128" fill="var(--paper)" role="img" aria-label="Space for the cover image of the book"/>
      <text class="front-type" font-size="17" font-weight="700" fill="var(--ink)">
        <textPath href="#type-arc" startOffset="50%" text-anchor="middle">TYPE OF WORK</textPath>
      </text>
      <text class="front-image-label" x="200" y="398" text-anchor="middle" font-size="20" font-weight="700" fill="var(--ink)">YOUR IMAGE</text>
      <text class="front-author" x="200" y="606" text-anchor="middle" font-size="15" font-weight="700" fill="var(--white)">AUTHOR</text>
    </svg>
  </main>
</body>
</html>
```